Sundial Bail Bonds Signboard Ad

I need a signboard ad that will be posted at a jail. We are a bail bond company and we bail people out of jail. The inmate/customer will call our company when they see our signboard ad posted inside a jail. The goal of the signboard ad is to get the attention of a person in custody and to stand out from the competition. The signboard ad is about 5x7. Open to any colors that will make it stand out. The content of the signboard ad must have "Sundial Bail Bonds" and our company phone number: (555) 318-2746. We want to emphasize we can get them out of jail quick and fast, was thinking maybe a catch phrase of "Sundial outta Jail" or "Sundial to Freedom". We don't have a logo. I will upload an attachment to show what the competition looks like. As you will see in the upload, my ad will go along with my competition. Also, I'm open to any creative ideas that will make my signboard ad stand out. Thank You.

Target Market(s)

People in jail.

Requirements
Must have
• Sundial Bail Bonds

(555) 318-2746
Nice to have
• I'm open to catch phrases that will get attention, for example "Sundial outta Jail" or "Sundial to Freedom". I do not have a company logo, if you can create a company logo, would be nice, was thinking an image of a rocket blasting off, The name of company is Sundial Bail Bonds.

```html
<!DOCTYPE html>
<html lang="en">
<head>
<meta charset="utf-8">
<title>Sundial Bail Bonds Signboard</title>
<link rel="stylesheet" href="https://fonts.googleapis.com/css2?family=Poppins:wght@700;800&family=Oswald:wght@600&display=swap">
<style>
  :root {
    --page-bg: #dde4eb;
    --sign-blue: #355ce6;
    --sign-deep: #254fc0;
    --sign-deep-light: #2d58cf;
    --accent-yellow: #fdb913;
    --ink-white: #ffffff;
  }
  html, body {
    margin: 0;
    padding: 0;
    width: 1200px;
    height: 1200px;
    overflow: hidden;
    background: var(--page-bg);
  }
  .signboard {
    position: absolute;
    left: 0;
    top: 171px;
    width: 1200px;
    height: 857px;
    background: var(--sign-blue);
    overflow: hidden;
  }
  .illustration-area {
    position: absolute;
    inset: 0;
  }
  .brand {
    position: absolute;
    left: 941px;
    top: 48px;
    display: flex;
    align-items: center;
    gap: 10px;
  }
  .brand-dot {
    width: 54px;
    height: 54px;
    border-radius: 50%;
    background: var(--accent-yellow);
  }
  .brand-name {
    font-family: "Poppins", sans-serif;
    font-weight: 700;
    font-size: 19px;
    line-height: 21px;
    letter-spacing: 1.5px;
    color: var(--ink-white);
    text-transform: uppercase;
  }
  .headline {
    position: absolute;
    left: 70px;
    top: 68px;
    margin: 0;
    font-family: "Poppins", sans-serif;
    font-weight: 800;
    font-size: 178px;
    line-height: 179px;
    letter-spacing: 2px;
    color: var(--ink-white);
    text-transform: uppercase;
  }
  .headline span { display: block; }
  .headline .highlight { color: var(--accent-yellow); }
  .phone {
    position: absolute;
    left: 71px;
    top: 628px;
    margin: 0;
    font-family: "Oswald", sans-serif;
    font-weight: 600;
    font-size: 66px;
    line-height: 80px;
    letter-spacing: 5px;
    color: var(--accent-yellow);
  }
</style>
</head>
<body>
  <main class="signboard">
    <svg class="illustration-area" width="1200" height="857" viewBox="0 0 1200 857">
      <defs>
        <linearGradient id="scene-tone" x1="0" y1="1" x2="1" y2="0">
          <stop offset="0" stop-color="var(--sign-deep)"/>
          <stop offset="1" stop-color="var(--sign-deep-light)"/>
        </linearGradient>
      </defs>
      <path class="scene-placeholder" role="img" aria-label="Illustration of a person walking free through opened jail cell bars" fill="url(#scene-tone)" d="M457,857 C460,760 520,690 614,666 C660,655 700,651 760,618 C820,585 870,520 917,461 C960,405 1000,360 1063,322 C1110,303 1160,302 1200,307 L1200,857 Z"/>
    </svg>

    <div class="brand">
      <div class="brand-dot"></div>
      <div class="brand-name">Sundial<br>Bail Bonds</div>
    </div>

    <h1 class="headline">
      <span>Sundial</span>
      <span class="highlight">Outta</span>
      <span>Jail</span>
    </h1>

    <p class="phone">(555) 318-2746</p>
  </main>
</body>
</html>
```